Spa needs a storefront sticker design

For our city spa we need window stickers for the shop window.
The window stickers must fill the entire windows.
What we have in mind is that our logo is visible in the middle with graphic shapes surrounding it to stand out extra on the main street. The design is going to be printed in white and cut out. To give an impression of what we have in mind, our logo is attached with various example designs.
please supply your final file in the following extensions: – Eps file (*.eps) – Photoshop file (*.psd) – Adobe Portable Document (*.pdf) – Jpeg file ( *.jpg, *.jpeg) – Tiff file (*.tif, *.tiff)– Text in letter outlines
A photo of the shop window will be added tomorrow, including the exact dimensions so that the design can be adjusted accordingly
Look and feel
Each slider illustrates characteristics of the customer's brand and the style your logo design should communicate.

```html
<!DOCTYPE html>
<html lang="en">
<head>
<meta charset="utf-8">
<title>Storefront Cut-Out Signage</title>
<link rel="stylesheet" href="https://fonts.googleapis.com/css2?family=Didact+Gothic&family=Prata&display=swap">
<style>
  :root {
    --board: #4b4b4b;
    --board-edge: #3a3a3a;
    --heading: #cfcfcf;
    --note: #ffffff;
    --vinyl: #ffffff;
    --brand-grey: #7b7b7b;
    --glass-top: #8a8480;
    --glass-mid: #7d7f82;
    --glass-low: #6e6964;
  }
  * { margin: 0; padding: 0; box-sizing: border-box; }
  html, body { width: 1200px; height: 928px; overflow: hidden; }
  body {
    background: var(--board);
    border: 1px solid var(--board-edge);
    position: relative;
    font-family: "Didact Gothic", sans-serif;
  }
  .board-title {
    position: absolute;
    left: 63px;
    top: 318px;
    color: var(--heading);
    font-size: 35px;
    line-height: 43px;
    font-weight: 400;
    letter-spacing: 0.5px;
  }
  .board-notes {
    position: absolute;
    left: 69px;
    top: 693px;
    color: var(--note);
    font-size: 16px;
    line-height: 21.5px;
    list-style: none;
  }
  .window-sticker {
    position: absolute;
    left: 521px;
    top: 137px;
    width: 601px;
    height: 680px;
  }
  .window-sticker svg { display: block; }
  .brand-name {
    font-family: "Prata", serif;
    font-size: 44px;
    letter-spacing: 8px;
    fill: var(--brand-grey);
  }
</style>
</head>
<body>
  <h1 class="board-title">STORE FRONT<br>CUT-OUT<br>SINAGE DESIGN</h1>

  <ul class="board-notes">
    <li>N:B</li>
    <li>Raw Files are ready.</li>
    <li>Ready to Print</li>
    <li>NO BACKGROUND AT ALL</li>
    <li>This is only a Preview.</li>
  </ul>

  <div class="window-sticker">
    <svg width="601" height="680" viewBox="0 0 601 680">
      <defs>
        <linearGradient id="glass" x1="0" y1="0" x2="0" y2="1">
          <stop offset="0" stop-color="var(--glass-top)"/>
          <stop offset="0.5" stop-color="var(--glass-mid)"/>
          <stop offset="1" stop-color="var(--glass-low)"/>
        </linearGradient>
      </defs>

      <rect class="window-glass" width="601" height="680" fill="url(#glass)"
            role="img" aria-label="Spa treatment room seen through the shop window"/>

      <rect class="sticker-frame" x="19" y="17" width="556" height="639"
            fill="none" stroke="var(--vinyl)" stroke-width="2"/>

      <path class="sticker-blob blob-top" d="M601 0 L601 140 C560 190 500 200 470 195 C430 190 414 150 416 110 C418 60 440 10 480 0 Z" fill="var(--vinyl)"/>
      <path class="sticker-blob blob-bottom" d="M0 540 C60 510 140 505 165 535 C190 570 160 640 120 680 L0 680 Z" fill="var(--vinyl)"/>

      <g class="foliage" role="img" aria-label="White cut-out tropical leaves and flowers" fill="var(--vinyl)" fill-opacity="0.55">
        <path d="M22 80 C50 60 80 80 85 130 C90 170 70 200 40 210 C25 200 20 150 22 80 Z"/>
        <path d="M110 17 L440 17 C400 60 340 80 300 120 C280 140 260 150 240 150 C200 130 160 100 120 60 Z"/>
        <circle cx="406" cy="189" r="13"/>
        <path d="M548 180 C565 190 570 210 570 230 L550 232 C538 215 538 195 548 180 Z"/>
        <path d="M22 460 C40 460 50 480 45 505 L22 510 Z"/>
        <circle cx="167" cy="483" r="13"/>
        <path d="M225 480 C300 520 380 560 420 600 C450 620 420 645 400 640 C320 630 240 640 165 645 C200 600 230 560 225 480 Z"/>
        <path d="M520 450 C560 440 578 470 575 520 C570 580 545 610 515 600 C490 570 490 490 520 450 Z"/>
      </g>

      <rect class="logo-band" x="0" y="244" width="601" height="180" fill="var(--vinyl)"/>
      <text class="brand-name" x="300" y="352" text-anchor="middle">WILLOW</text>
    </svg>
  </div>
</body>
</html>
```